Business card for Drone Aerial

I need a business card designed keeping in mind I want to do post cards also with a similar design.
Both sides of the card would be cool.
I have a vortel 8 max and would like a picture of it on the front of the card. Similar to one I attached.
I really like the look of a drone in the air and the background pic a little blurry. I attached a few images as IDEAS.
Some special things I want to be on the card additional to the normal business card info:
"Aerial Photography" or "Low Altitude Aerial Photography"?
"KTO# 58203917"

I like modern and creative. My Favorite color is blue and I like blue on white.
I do not have a business name and am not going to have one. When they read "Aerial Photography" and see the drone and image they will know what the card is for.

FYI, The attached pictures are just images from pixelgrove and just samples/ideas.

Target Market(s)

Real estate, construction, events

Industry/Entity Type

Business

Contact Information for Business Card

Also Definitely want to contain, my name, my number and email address.

Requirements
Must have
• "KTO# 58203917"
• "Aerial Photography"

```html
<!DOCTYPE html>
<html lang="en">
<head>
<meta charset="utf-8">
<title>Aerial Photography – Business Card</title>
<link href="https://fonts.googleapis.com/css2?family=Lato:wght@300;400;700;900&family=Great+Vibes&display=swap" rel="stylesheet">
<style>
  :root {
    --page: #e9ecef;
    --sky: #2f8fd8;
    --sky-light: #7cc4f2;
    --night: #2a2a2e;
    --night-soft: #3b3b40;
    --accent: #4aa3e6;
    --white: #ffffff;
    --muted: #d7dde3;
  }
  * { box-sizing: border-box; margin: 0; padding: 0; }
  html, body { width: 800px; height: 1200px; overflow: hidden; }
  body {
    background: var(--page);
    font-family: "Lato", sans-serif;
    display: flex;
    flex-direction: column;
    align-items: center;
    justify-content: center;
    gap: 80px;
  }
  .card {
    position: relative;
    width: 700px;
    height: 400px;
    overflow: hidden;
    background: var(--night);
    box-shadow: 0 10px 30px rgba(0,0,0,.25);
    color: var(--white);
  }

  /* Front */
  .front-photo {
    position: absolute; inset: 0;
    background:
      radial-gradient(ellipse 260px 200px at 64% 34%, rgba(255,255,255,.55), rgba(255,255,255,0) 70%),
      linear-gradient(160deg, var(--sky-light) 0%, var(--sky) 45%, #1f6fb3 100%);
  }
  .front-shade {
    position: absolute; inset: 0;
    background: linear-gradient(200deg, rgba(42,42,46,0) 30%, rgba(42,42,46,.85) 55%, var(--night) 75%);
  }
  .bracket { position: absolute; width: 24px; height: 24px; border-color: var(--accent); border-style: solid; border-width: 0; }
  .bracket.tl { left: 40px; top: 170px; border-left-width: 3px; border-top-width: 3px; }
  .bracket.bl { left: 40px; bottom: 40px; border-left-width: 3px; border-bottom-width: 3px; }
  .bracket.tr { left: 440px; top: 170px; border-right-width: 3px; border-top-width: 3px; }
  .bracket.br { left: 440px; bottom: 40px; border-right-width: 3px; border-bottom-width: 3px; }

  .front-text { position: absolute; left: 70px; top: 160px; width: 380px; }
  .tagline { font-family: "Great Vibes", cursive; font-size: 30px; color: var(--muted); margin-bottom: 4px; }
  .title-thin { font-weight: 300; font-size: 34px; letter-spacing: 3px; line-height: 1; }
  .title-bold { font-weight: 900; font-size: 40px; letter-spacing: 1px; line-height: 1.05; }
  .subtitle { font-size: 12px; letter-spacing: 3px; color: var(--muted); margin-top: 4px; }
  .divider { position: relative; height: 1px; background: var(--muted); width: 260px; margin: 14px 0 12px; }
  .divider::after { content: ""; position: absolute; left: 126px; top: -4px; width: 9px; height: 9px; border-radius: 50%; background: var(--white); }
  .name { font-weight: 700; font-size: 17px; letter-spacing: 3px; text-transform: uppercase; }
  .contact { font-size: 14px; letter-spacing: 1.5px; color: var(--muted); line-height: 1.5; }

  /* Back */
  .back-photos { position: absolute; inset: 0; }
  .back-shade {
    position: absolute; inset: 0;
    background: linear-gradient(90deg, rgba(20,20,24,.15) 0%, rgba(20,20,24,.45) 40%, rgba(20,20,24,.15) 100%);
  }
  .back-text { position: absolute; left: 220px; top: 110px; }
  .back-text .title-thin { font-size: 40px; }
  .back-text .title-bold { font-size: 50px; }
  .license { font-size: 15px; letter-spacing: 4px; margin-top: 6px; color: var(--white); }
  .services {
    position: absolute; left: 0; right: 0; bottom: 0;
    background: rgba(30,30,34,.7);
    padding: 12px 30px;
    font-size: 13px; letter-spacing: 1px; line-height: 1.7; text-align: center;
  }
  .services span + span::before { content: "|"; margin: 0 10px; color: var(--accent); }
</style>
</head>
<body>

  <section class="card card-front">
    <div class="front-photo" role="img" aria-label="Photo of a white quadcopter drone flying against a softly blurred blue sky"></div>
    <div class="front-shade"></div>
    <span class="bracket tl"></span><span class="bracket bl"></span>
    <span class="bracket tr"></span><span class="bracket br"></span>
    <div class="front-text">
      <p class="tagline">Reach For The Sky</p>
      <h1 class="title-thin">AERIAL</h1>
      <h2 class="title-bold">PHOTOGRAPHY</h2>
      <p class="subtitle">Low Altitude</p>
      <div class="divider"></div>
      <p class="name">Marcus Delaney</p>
      <p class="contact">hello@skyframe-media.com</p>
      <p class="contact">(555) 318 472</p>
    </div>
  </section>

  <section class="card card-back">
    <svg class="back-photos" width="700" height="400" viewBox="0 0 700 400" role="img" aria-label="Three slanted aerial landscape photos: a coastline with beach, a mountain valley with fields, and a turquoise lagoon">
      <defs>
        <linearGradient id="strip-coast" x1="0" y1="0" x2="0" y2="1">
          <stop offset="0" stop-color="#9cc8e6"/>
          <stop offset=".55" stop-color="#5e8fae"/>
          <stop offset="1" stop-color="#b0884a"/>
        </linearGradient>
        <linearGradient id="strip-valley" x1="0" y1="0" x2="0" y2="1">
          <stop offset="0" stop-color="#c9c4cc"/>
          <stop offset=".4" stop-color="#8a7560"/>
          <stop offset=".75" stop-color="#c79a3c"/>
          <stop offset="1" stop-color="#4f7a3c"/>
        </linearGradient>
        <linearGradient id="strip-lagoon" x1="0" y1="0" x2="0" y2="1">
          <stop offset="0" stop-color="#cfe3ef"/>
          <stop offset=".5" stop-color="#3fb4cf"/>
          <stop offset="1" stop-color="#1f6f95"/>
        </linearGradient>
      </defs>
      <polygon points="0,0 200,0 140,400 0,400" fill="url(#strip-coast)"/>
      <polygon points="212,0 500,0 440,400 152,400" fill="url(#strip-valley)"/>
      <polygon points="512,0 700,0 700,400 452,400" fill="url(#strip-lagoon)"/>
      <polygon points="200,0 212,0 152,400 140,400" fill="#2a2a2e"/>
      <polygon points="500,0 512,0 452,400 440,400" fill="#2a2a2e"/>
    </svg>
    <div class="back-shade"></div>
    <div class="back-text">
      <h1 class="title-thin">AERIAL</h1>
      <h2 class="title-bold">PHOTOGRAPHY</h2>
      <p class="license">KTO# 58203917</p>
    </div>
    <p class="services">
      <span>Construction Aerial Footage</span><span>New Home Imagery</span><span>Maximize Your Listing</span><br>
      <span>Entertainment Events</span><span>Real Estate Developments</span><span>Sporting Events</span>
    </p>
  </section>

</body>
</html>
```